Bookcover: Ways to Turn Into a Bold Pathfinder

I am publishing a super-low-cost innovation book for €4,99 on Pageleaf Open Press to help everyone become a great innovator: young ambitious people without college education nor a big budget. Do you want to help me?

Brief:
Design a book cover 1600 x 2560 pixels for POP.
Main title: Ways to Turn Into a Bold Pathfinder
Sub title: Attitude - Lessons - Craft & Methods
Author: Maarten de Kolkema
Design: captive, and appealing to everyone
Target Group: young ambitious people without college education

For pageleaf please format the height/width ratio of 1.6:1

```html
<!DOCTYPE html>
<html lang="en">
<head>
<meta charset="utf-8">
<title>Ways to Turn Into a Bold Pathfinder — Book Cover</title>
<link rel="stylesheet" href="https://fonts.googleapis.com/css2?family=Bebas+Neue&display=swap">
<style>
  :root {
    --cover-yellow: #e6e000;
    --ink-black: #000000;
    --paper-white: #ffffff;
    --subtitle-white: #eeeef4;
    --stage: #ffffff;
    --illustration-tone: #d9d400;
  }
  * { box-sizing: border-box; margin: 0; padding: 0; }
  html, body {
    width: 1200px;
    height: 1092px;
    overflow: hidden;
    background: var(--stage);
  }
  .cover {
    position: absolute;
    left: 287px;
    top: 46px;
    width: 625px;
    height: 1000px;
    background: var(--cover-yellow);
    overflow: hidden;
    font-family: "Bebas Neue", "Arial Narrow", sans-serif;
    color: var(--ink-black);
  }
  .title {
    position: absolute;
    inset: 0;
    font-weight: 400;
  }
  .title__line {
    position: absolute;
    left: 0;
    width: 100%;
    text-align: center;
    line-height: 1;
    white-space: nowrap;
  }
  .title__line--small { top: 36px; font-size: 96px; }
  .title__line--medium { top: 122px; font-size: 112px; }
  .title__line--large { top: 216px; font-size: 156px; letter-spacing: -1px; }
  .bulb-illustration {
    position: absolute;
    top: 372px;
    left: 40px;
    width: 545px;
    height: 178px;
    border-radius: 6px;
    background: linear-gradient(180deg, var(--cover-yellow) 0%, var(--illustration-tone) 50%, var(--cover-yellow) 100%);
  }
  .band {
    position: absolute;
    top: 570px;
    left: 0;
    width: 625px;
    height: 275px;
  }
  .band svg { display: block; width: 100%; height: 100%; }
  .subtitle {
    position: absolute;
    top: 660px;
    left: 0;
    width: 100%;
    text-align: center;
    color: var(--subtitle-white);
    font-size: 54px;
    letter-spacing: 3px;
    line-height: 1.05;
  }
  .subtitle span { display: block; }
  .author {
    position: absolute;
    top: 890px;
    left: 0;
    width: 100%;
    text-align: center;
    font-size: 56px;
    letter-spacing: 2px;
    line-height: 1;
  }
</style>
</head>
<body>
  <main class="cover">
    <h1 class="title">
      <span class="title__line title__line--small">Ways to Turn</span>
      <span class="title__line title__line--medium">Into a Bold</span>
      <span class="title__line title__line--large">PATHFINDER</span>
    </h1>

    <div class="bulb-illustration" role="img" aria-label="Illustration of five hanging light bulbs whose wires untangle from knotted scribbles into a straight line"></div>

    <div class="band" aria-hidden="true">
      <svg viewBox="0 0 625 275" preserveAspectRatio="none">
        <polygon fill="#ffffff" points="0,10 30,4 58,12 90,6 118,14 150,8 185,12 210,2 240,10 272,6 300,12 330,4 362,10 395,6 420,14 452,8 480,12 515,4 545,10 580,6 605,12 625,8 625,262 598,268 570,260 540,270 508,262 478,268 446,258 415,266 385,262 352,270 320,262 290,266 258,258 228,268 196,262 165,270 132,262 100,268 70,260 40,268 12,262 0,266"/>
        <polygon fill="#000000" points="0,18 28,12 60,20 92,14 120,22 152,16 186,20 212,10 242,18 272,14 302,20 332,12 362,18 396,14 422,22 452,16 482,20 516,12 546,18 580,14 606,20 625,16 625,254 598,260 570,252 540,262 508,254 478,260 446,250 415,258 385,254 352,262 320,254 290,258 258,250 228,260 196,254 165,262 132,254 100,260 70,252 40,260 12,254 0,258"/>
      </svg>
    </div>

    <p class="subtitle">
      <span>Attitude - Lessons</span>
      <span>Craft &amp; Methods</span>
    </p>

    <p class="author">Maarten de Kolkema</p>
  </main>
</body>
</html>
```